Meridane Haulage - Website

A clean, not cluttered informative website for our business. We specialize in the transportation of radioactive materials across North America. The site is mostly for information about our company and will not be used to attract business but will be used to attract employee's mainly drivers. Driver's are very hard to find in our area. One of the pages needs to be a job's posting page with an apply now button. Either an application can be filled out there or a resume can be uploaded which ever functionality works better. I would like a website that I can easily edit, ability to change text and photos.

Number of Pages Required

5+ page

Colors

Designer to choose colors to be used in the design.

Requirements
Must have
• Home - About - Services - Jobs - Contact pages
• A way prospective employee's can apply or upload their resume to be emailed to me
• Very clean apperance
Should not have
• I don't want it to be busy

```html
<!DOCTYPE html>
<html lang="en">
<head>
<meta charset="utf-8">
<title>Meridane Haulage</title>
<link rel="stylesheet" href="https://fonts.googleapis.com/css2?family=Michroma&family=Jost:wght@400;500;600&display=swap">
<style>
:root{
  --ink:#1e1e1e;
  --bar:#222323;
  --text:#2a2a2a;
  --muted:#555;
  --white:#fff;
  --line:#9a9a9a;
  --band:#c9c9c9;
  --footer:#2b2e31;
  --btn:#1c1c1c;
  --btn-knob:#6a6a6a;
}
*{box-sizing:border-box;margin:0;padding:0}
html,body{width:1200px;height:2932px;overflow:hidden}
body{position:relative;background:var(--white);font-family:"Jost",Arial,sans-serif;color:var(--text)}
.abs{position:absolute}
.site-header{left:0;top:0;width:1200px;height:107px;background:var(--bar)}
.brand{left:146px;top:30px;color:var(--white);font-family:"Michroma",sans-serif;font-size:19px;line-height:24px;letter-spacing:3px}
.phone{left:875px;top:18px;color:#ddd;font-family:"Michroma",sans-serif;font-size:17px;letter-spacing:1px;display:flex;align-items:center;gap:12px}
.nav{top:62px;color:#e6e6e6;font-family:"Michroma",sans-serif;font-size:13px;letter-spacing:1.5px}
.nav.active{color:var(--white);border-bottom:2px solid var(--white);padding-bottom:6px}
.hero{left:0;top:107px;width:1200px;height:567px;background:linear-gradient(180deg,#b9bcbf 0%,#8d8c88 45%,#5c5e60 100%)}
.hero-text{left:0;width:1200px;top:490px;text-align:center;color:var(--white);font-family:"Jost",sans-serif;font-weight:500;font-size:35px;line-height:54px;text-shadow:0 2px 4px rgba(0,0,0,.5)}
.dots{left:574px;top:615px;display:flex;gap:6px}
.dots span{width:11px;height:11px;border-radius:50%;background:#bbb;border:1px solid #777}
.dots span.on{background:#333}
.section-title{left:0;width:1200px;text-align:center;font-family:"Michroma",sans-serif;font-size:33px;color:#3c3c3c;letter-spacing:2px}
.rule{height:2px;background:var(--line)}
.lead{left:170px;width:860px;top:836px;text-align:center;font-size:16.5px;line-height:26px;color:var(--ink)}
.small{left:176px;width:848px;top:903px;text-align:center;font-size:12.5px;line-height:19px;color:var(--muted)}
.btn{display:flex;align-items:center;justify-content:space-between;height:36px;border-radius:18px;background:var(--btn);color:var(--white);font-size:14px;padding:0 4px 0 16px}
.btn i{width:28px;height:28px;border-radius:50%;background:var(--btn-knob);display:flex;align-items:center;justify-content:center}
.band{left:0;top:1090px;width:1200px;height:1151px;background:linear-gradient(180deg,#d2d2d2 0%,#bfbfbf 40%,#8e9092 75%,#6d6f71 100%)}
.card{background:var(--white);border-radius:4px;box-shadow:0 4px 14px rgba(0,0,0,.25);overflow:hidden}
.photo{background:linear-gradient(160deg,#7d93ad 0%,#9aa0a4 55%,#8a7b62 100%)}
.photo.cab{background:linear-gradient(200deg,#c8d4e2 0%,#eef0f2 45%,#9a9c9e 100%)}
.card h3{font-weight:500;font-size:18px;color:var(--ink);margin-bottom:14px}
.card p{font-size:12.5px;line-height:20px;color:var(--muted);margin-bottom:14px}
.ticks{list-style:none;font-size:12.5px;line-height:20.5px;color:var(--muted)}
.ticks li{display:flex;align-items:center;gap:9px}
.ticks li::before{content:"";width:10px;height:10px;border:1.5px solid #444;border-radius:2px;background:linear-gradient(135deg,transparent 45%,#444 45%,#444 55%,transparent 55%)}
.cta-head{left:0;width:1200px;top:2310px;text-align:center;font-family:"Michroma",sans-serif;font-size:28px;line-height:46px;color:#333;letter-spacing:2px}
.footer{left:0;top:2470px;width:1200px;height:462px}
.f-title{font-family:"Michroma",sans-serif;font-size:12.5px;color:#cfcfcf;letter-spacing:1px}
.f-list{list-style:none;font-size:12px;line-height:28px;color:#ddd}
.f-list li::before{content:"•";margin-right:10px}
.f-item{display:flex;gap:14px;font-size:12px;line-height:18px;color:#ddd}
.social{display:flex;align-items:center;gap:12px;font-size:12px;color:#ddd;letter-spacing:.5px}
.social i{width:30px;height:30px;border-radius:50%;background:#474b4f}
.map{left:645px;top:2708px;width:199px;height:123px;border-radius:3px;background:linear-gradient(135deg,#e6e8e2,#d4dccd)}
.copyright{left:0;top:2896px;width:1200px;height:36px;background:#5a5d60;color:#ddd;text-align:center;font-size:11.5px;line-height:36px}
</style>
</head>
<body>

<header class="abs site-header"></header>
<div class="abs brand">MERIDANE<br>HAULAGE</div>
<div class="abs phone">
  <svg width="18" height="18" viewBox="0 0 24 24"><path fill="#ddd" d="M6.6 10.8a15.1 15.1 0 006.6 6.6l2.2-2.2a1 1 0 011-.25 11.4 11.4 0 003.6.57 1 1 0 011 1V20a1 1 0 01-1 1A17 17 0 013 4a1 1 0 011-1h3.5a1 1 0 011 1c0 1.25.2 2.45.57 3.6a1 1 0 01-.25 1z"/></svg>
  555-014-2736
</div>
<nav>
  <span class="abs nav active" style="left:487px">HOME</span>
  <span class="abs nav" style="left:592px">ABOUT</span>
  <span class="abs nav" style="left:711px">SERVICES</span>
  <span class="abs nav" style="left:860px">JOBS</span>
  <span class="abs nav" style="left:957px">CONTACT</span>
</nav>

<section>
  <div class="abs hero" role="img" aria-label="Semi truck hauling radioactive material containers on a flatbed trailer"></div>
  <svg class="abs" style="left:0;top:560px" width="1200" height="116" viewBox="0 0 1200 116"><path fill="#fff" d="M0 56 C260 100 520 110 760 70 C950 38 1080 30 1200 52 L1200 116 L0 116 Z"/></svg>
  <div class="abs hero-text">Specializing in the Transportation of Radioactive<br>Materials Across North America</div>
  <div class="abs dots"><span class="on"></span><span></span><span></span></div>
</section>

<section>
  <h2 class="abs section-title" style="top:748px">ABOUT MERIDANE HAULAGE</h2>
  <div class="abs rule" style="left:469px;top:803px;width:262px"></div>
  <p class="abs lead">Lorem ipsum dolor sit amet, consectetuer adipiscing elit, sed diam nonummy nibh euismod tincidunt ut laoreet dolore magna aliquam erat volutpat. Ut wisi enim ad minim veniam, quis nostrud exerci tation</p>
  <p class="abs small">suscipit lobortis nisl ut aliquip ex ea commodo consequat. Duis autem vel eum iriure dolor in hendrerit in vulputate velit esse molestie consequat, vel illum dolore eu feugiat nulla facilisis at vero eros et accumsan et iusto odio dignissim qui blandit praesent luptatum zzril delenit augue duis dolore te feugait nulla facilisi. elit, sed diam nonummy nibh euismod tincidunt ut laoreet dolore magna aliquam erat volutpat. Ut wisi enim ad minim veniam,</p>
  <a class="abs btn" style="left:537px;top:985px;width:124px">Read More <i><svg width="12" height="10" viewBox="0 0 12 10"><path d="M1 1l4 4-4 4M6 1l4 4-4 4" stroke="#fff" stroke-width="1.6" fill="none"/></svg></i></a>
</section>

<div class="abs band" role="img" aria-label="Faded background of parked white truck cabs"></div>

<section>
  <h2 class="abs section-title" style="top:1160px">SERVICE WE PROVIDE</h2>
  <div class="abs rule" style="left:469px;top:1213px;width:262px"></div>
  <div class="abs card" style="left:143px;top:1243px;width:916px;height:365px">
    <div class="abs photo" style="left:0;top:0;width:455px;height:365px" role="img" aria-label="Flatbed truck carrying yellow radioactive transport drums"></div>
    <div class="abs" style="left:492px;top:32px;width:395px">
      <h3>Transportation of Radioactive Materials</h3>
      <p>Lorem ipsum dolor sit amet, consectetuer adipiscing elit, sed diam no nummy nibh euismod tincidunt ut laoreet dolore magna</p>
      <p>Lorem ipsum dolor sit amet, consectetuer adipiscing elit, sed diammony nibh euismod tincidunt ut laoreet dolore magna suscipit lobortis nisl ut aliquip ex ea commodo consequat.</p>
      <ul class="ticks"><li>injected humour</li><li>true generator on the Internet</li><li>Lorem Ipsum generators</li><li>Many desktop publishing packages</li></ul>
      <a class="btn" style="width:124px;margin-top:14px">Know More <i><svg width="12" height="10" viewBox="0 0 12 10"><path d="M1 1l4 4-4 4M6 1l4 4-4 4" stroke="#fff" stroke-width="1.6" fill="none"/></svg></i></a>
    </div>
  </div>
</section>

<section>
  <h2 class="abs section-title" style="top:1682px">JOIN OUR TEAM</h2>
  <div class="abs rule" style="left:469px;top:1735px;width:262px"></div>
  <div class="abs card" style="left:143px;top:1766px;width:916px;height:364px">
    <div class="abs" style="left:34px;top:36px;width:420px">
      <h3>Driving Opportunities</h3>
      <p style="margin-bottom:10px">Lorem ipsum dolor sit amet, consectetuer adipiscing elit, sed diamnony nibh euismod tincidunt ut laoreet.</p>
      <p style="color:var(--ink);font-size:13px">To speak with the Driver Recruiting Department, call 555.014.2736</p>
      <ul class="ticks"><li>Drivers Apply Online</li><li>Drivers Benefits</li><li>Driving Career Path</li><li>Drivers Frequently Asked Questions</li><li>Drivers Incentive Programs</li><li>Paid Apprenticeship CDL Training</li></ul>
      <a class="btn" style="width:124px;margin-top:14px">Apply Now <i><svg width="12" height="10" viewBox="0 0 12 10"><path d="M1 1l4 4-4 4M6 1l4 4-4 4" stroke="#fff" stroke-width="1.6" fill="none"/></svg></i></a>
    </div>
    <div class="abs photo cab" style="left:453px;top:0;width:463px;height:364px" role="img" aria-label="Driver leaning out of a white truck cab window"></div>
  </div>
</section>

<section>
  <h2 class="abs cta-head">LOREM IPSUM DOLOR SIT AMET CIDUNT UT<br>MAGNA ALIQUAM ERAT VOLUTPAT</h2>
  <a class="abs btn" style="left:512px;top:2452px;width:176px">Contact Us Today <i><svg width="12" height="10" viewBox="0 0 12 10"><path d="M1 1l4 4-4 4M6 1l4 4-4 4" stroke="#fff" stroke-width="1.6" fill="none"/></svg></i></a>
</section>

<footer>
  <svg class="abs footer" viewBox="0 0 1200 462" role="img" aria-label="City skyline at night behind footer">
    <path fill="#8a8c8e" d="M0 0 C120 40 260 60 420 62 C700 66 980 80 1200 122 L1200 462 L0 462 Z"/>
    <path fill="#fff" d="M0 48 C180 90 360 100 560 96 C820 92 1020 110 1200 140 L1200 462 L0 462 Z"/>
    <path fill="#3a3d40" d="M0 70 C180 110 360 118 560 112 C820 106 1020 124 1200 152 L1200 462 L0 462 Z"/>
    <rect x="0" y="150" width="1200" height="312" fill="var(--footer)"/>
  </svg>
  <div class="abs f-title" style="left:145px;top:2657px">QUICK LINKS</div>
  <ul class="abs f-list" style="left:145px;top:2694px"><li>Home</li><li>About</li><li>Services</li><li>Jobs</li><li>Contact</li></ul>

  <div class="abs f-title" style="left:363px;top:2657px">CONTACT DETAILS</div>
  <div class="abs" style="left:363px;top:2702px;display:flex;flex-direction:column;gap:22px">
    <div class="f-item"><svg width="10" height="14" viewBox="0 0 10 14"><path fill="#ddd" d="M5 0a5 5 0 015 5c0 4-5 9-5 9S0 9 0 5a5 5 0 015-5zm0 3a2 2 0 100 4 2 2 0 000-4z"/></svg><span>88 Fenwick Yard Road<br>Calderbrook, North America</span></div>
    <div class="f-item"><svg width="12" height="12" viewBox="0 0 24 24"><path fill="#ddd" d="M6.6 10.8a15.1 15.1 0 006.6 6.6l2.2-2.2a1 1 0 011-.25 11.4 11.4 0 003.6.57 1 1 0 011 1V20a1 1 0 01-1 1A17 17 0 013 4a1 1 0 011-1h3.5a1 1 0 011 1c0 1.25.2 2.45.57 3.6a1 1 0 01-.25 1z"/></svg><span>555-014-2736</span></div>
    <div class="f-item" style="margin-top:12px"><svg width="13" height="10" viewBox="0 0 13 10"><rect width="13" height="10" rx="1" fill="#ddd"/><path d="M0 0l6.5 5L13 0" stroke="#2b2e31" fill="none"/></svg><span>info@meridanehaulage.com</span></div>
  </div>

  <div class="abs f-title" style="left:645px;top:2657px">LOCATION MAP</div>
  <div class="abs map" role="img" aria-label="Street map showing the company location"></div>

  <div class="abs f-title" style="left:946px;top:2657px">FOLLOW US</div>
  <div class="abs" style="left:946px;top:2704px;display:flex;flex-direction:column;gap:16px">
    <div class="social"><i></i>PEERBOOK</div>
    <div class="social"><i></i>CHIRPER</div>
    <div class="social"><i></i>WORKLINK</div>
  </div>
  <div class="abs copyright">Copyright © 2019 Meridane Haulage All Rights Reserved.</div>
</footer>

</body>
</html>
```